Business Card Design Project

I am a consultant mostly to mining or large infrastructure companies - so a little conservative. I am looking for a business card with a logo. I will then put the logo in my signature page for emails etc also.

The company is called Pellandre Capital and comprises Pellandre Offshore Pte Ltd based in SIngapore and Pellandre Consulting Pty Ltd based in Australia.

Pellandre is a beach in Byron Bay Australia. It has a large lighthouse above it which I would like included in the design. Beaches etc are not very professional or conservative but i think we could work the lighthouse in.

Here it is http://en.lorimapedia.org/wiki/Point_Hessary_Light

I will not have address details but will have 2x phones and 1 skype and 1x email address

```html
<!DOCTYPE html>
<html lang="en">
<head>
<meta charset="utf-8">
<title>Pellandre Capital – Business Cards</title>
<link rel="stylesheet" href="https://fonts.googleapis.com/css2?family=Carlito:wght@400;700&display=swap">
<style>
  :root {
    --navy: #0d3059;
    --sky: #a9cbef;
    --ink: #111418;
    --paper: #ffffff;
    --stage-light: #f7f7f5;
    --stage-dark: #c4c3bf;
  }
  * { margin: 0; padding: 0; box-sizing: border-box; }
  html, body { width: 1200px; height: 1000px; overflow: hidden; }
  body {
    position: relative;
    font-family: "Carlito", "Calibri", sans-serif;
    color: var(--ink);
    background: radial-gradient(ellipse 700px 560px at 860px 520px, var(--stage-light) 0%, #dcdcd9 60%, var(--stage-dark) 100%);
  }
  .card {
    position: absolute;
    width: 447px;
    height: 283px;
    background: var(--paper);
    box-shadow: 0 2px 6px rgba(0,0,0,0.18);
  }
  .card::after {
    content: "";
    position: absolute;
    left: 0; right: 0; bottom: 0;
    height: 6px;
    background: var(--navy);
  }
  .card--front-stacked { left: 134px; top: 198px; }
  .card--front-columns { left: 134px; top: 533px; }
  .card--back { left: 619px; top: 198px; width: 448px; background: var(--navy); }
  .card--back::after { background: var(--sky); height: 5px; }

  .brand {
    position: absolute;
    display: flex;
    align-items: center;
    gap: 10px;
    font-weight: 700;
    color: var(--navy);
    white-space: nowrap;
  }
  .brand__name { font-size: 28px; letter-spacing: -0.5px; }
  .brand__dot { width: 46px; height: 46px; border-radius: 50%; background: var(--navy); flex: none; }
  .card--front-stacked .brand { right: 22px; top: 51px; }
  .card--front-columns .brand { right: 22px; top: 54px; }
  .card--back .brand { left: 50%; top: 99px; transform: translateX(-50%); color: var(--paper); }
  .card--back .brand__name { font-size: 38px; }
  .card--back .brand__dot { width: 60px; height: 60px; background: var(--paper); }

  .holder { position: absolute; left: 21px; }
  .holder__name { font-size: 19px; font-weight: 700; line-height: 22px; }
  .holder__role { font-size: 15px; line-height: 19px; }
  .card--front-stacked .holder { top: 100px; }
  .card--front-columns .holder { top: 173px; }

  .contact { position: absolute; list-style: none; font-size: 13.5px; line-height: 18px; }
  .contact__web { font-weight: 700; color: var(--navy); }
  .card--front-stacked .contact { left: 21px; top: 174px; }
  .card--front-columns .contact { left: 205px; top: 174px; }

  .legal {
    position: absolute;
    left: 0; right: 0; top: 225px;
    text-align: center;
    color: var(--sky);
    font-size: 13.5px;
    font-weight: 700;
    line-height: 18px;
  }
</style>
</head>
<body>

<section class="card card--front-stacked">
  <div class="brand"><span class="brand__name">Pellandre Capital</span><span class="brand__dot"></span></div>
  <div class="holder">
    <p class="holder__name">Marcus Trevelyan</p>
    <p class="holder__role">Director and CEO</p>
  </div>
  <ul class="contact">
    <li>mtrevelyan@pellandre-capital.com</li>
    <li>(Sing) +65 9100 4827</li>
    <li>(Aust) +61 400 118 352</li>
    <li>(Skype) trevelyanmarcus70</li>
    <li class="contact__web">www.pellandre-capital.com</li>
  </ul>
</section>

<section class="card card--back">
  <div class="brand"><span class="brand__name">Pellandre Capital</span><span class="brand__dot"></span></div>
  <div class="legal">
    <p>Pellandre Consulting Pty Ltd (ACN 012 345 678)</p>
    <p>Pellandre Offshore Pte Ltd (Reg # 201100456K)</p>
  </div>
</section>

<section class="card card--front-columns">
  <div class="brand"><span class="brand__name">Pellandre Capital</span><span class="brand__dot"></span></div>
  <div class="holder">
    <p class="holder__name">Marcus Trevelyan</p>
    <p class="holder__role">Director and CEO</p>
  </div>
  <ul class="contact">
    <li>mtrevelyan@pellandre-capital.com</li>
    <li>(Sing) +65 9100 4827</li>
    <li>(Aust) +61 400 118 352</li>
    <li>(Skype) trevelyanmarcus70</li>
    <li class="contact__web">www.pellandre-capital.com</li>
  </ul>
</section>

</body>
</html>
```